Law Firm Website

We are looking to update our old, tired and very flat website. We have someone who will code and host the site but we need some design inspiration. The website will consist of no more than 2/3 pages, possibly with pop-ups for information. We already have all the blurb. We would like something distinctive, clean and eye-catching, using the purple and white theme that we already use on our firm stationery. Examples uploaded. Current website URL is www.dunmorewillett.example.

Industry/Entity Type

Law Firm

```html
<!DOCTYPE html>
<html lang="en">
<head>
<meta charset="utf-8">
<title>Dunmore + Willett Solicitors</title>
<link rel="stylesheet" href="https://fonts.googleapis.com/css2?family=Ubuntu:ital,wght@0,300;0,400;0,500;0,700;1,300;1,500&display=swap">
<style>
:root{
  --purple:#4f3a86;
  --purple-deep:#3f2d72;
  --purple-nav:#6a55a8;
  --purple-text:#553f95;
  --ink:#17302a;
  --grey-text:#6b6b6b;
  --soft-bg:#f8fafa;
  --band:#ececec;
  --line:#dcdcdc;
  --white:#ffffff;
}
*{margin:0;padding:0;box-sizing:border-box}
html,body{width:1024px;height:1200px;overflow:hidden}
body{font-family:"Ubuntu",sans-serif;background:var(--soft-bg);color:var(--grey-text);position:relative}
.topline{position:absolute;top:0;left:0;width:1024px;height:3px;background:var(--purple)}
.header{position:absolute;top:3px;left:0;width:1024px;height:102px;background:var(--white)}
.brand{position:absolute;left:135px;top:22px;color:var(--ink);font-weight:500}
.brand .name{font-size:38px;line-height:40px;letter-spacing:-.5px;display:block}
.brand .tag{font-size:19px;line-height:22px;margin-left:72px;display:block}
.reg{position:absolute;top:42px;font-size:11.5px;line-height:17px;padding-left:18px;border-left:1px solid var(--line);height:40px}
.reg small{display:block;color:#8c8c8c;font-size:11px}
.reg b{font-weight:400;color:var(--purple-text)}
.reg-auth{left:584px}
.reg-vat{left:759px}
.reg-vat b{font-size:12.5px}
.nav{position:absolute;top:105px;left:0;width:1024px;height:41px;background:linear-gradient(#7d69b6,var(--purple-nav) 60%,#5d4899);border-top:2px solid #8a8a8a}
.nav a{position:absolute;top:0;height:39px;line-height:39px;color:var(--white);font-size:12.5px;text-decoration:none}
.nav .active{left:135px;width:114px;text-align:center;background:rgba(255,255,255,.2)}
.hero{position:absolute;top:146px;left:0;width:1024px;height:432px;background:linear-gradient(180deg,#5e4d8c 0%,#c07a7a 28%,#6a3f6e 55%,#3c2a5c 100%)}
.hero .glow{position:absolute;inset:0;background:radial-gradient(ellipse at 22% 70%,rgba(240,150,60,.55),transparent 45%)}
.hero h1{position:absolute;left:519px;top:250px;color:var(--white);font-weight:300;font-size:32px;line-height:38px;letter-spacing:-.3px}
.card{position:absolute;top:514px;height:184px;background:var(--white);border:1px solid var(--line)}
.card-a{left:136px;width:368px}
.card-b{left:518px;width:371px}
.card .photo{position:absolute;left:0;top:0;width:157px;height:182px;background:linear-gradient(160deg,#9aa2ad,#4a5563)}
.card-b .photo{background:linear-gradient(160deg,#8a8a8a,#2a2a2a)}
.card h2{position:absolute;left:176px;top:22px;font-weight:300;font-size:19.5px;color:var(--purple-text)}
.card-b h2{left:171px}
.card p{position:absolute;left:176px;top:55px;width:182px;font-size:11.5px;line-height:16px;font-weight:300;color:#444}
.card-b p{left:171px;width:190px}
.card .more{position:absolute;left:175px;top:132px;padding:0 10px;height:26px;line-height:24px;border:1px solid #ccc;border-radius:13px;font-size:9px;color:#777;background:linear-gradient(#fff,#ececec)}
.card-b .more{left:170px}
.expertise-title{position:absolute;top:723px;left:0;width:1024px;text-align:center;font-weight:300;font-size:20px;color:#3b3b3b}
.expertise-intro{position:absolute;top:758px;left:262px;width:500px;text-align:center;font-size:9px;line-height:13px;color:#6e6e8a}
.area{position:absolute;width:200px;height:46px}
.area .icon{position:absolute;left:0;top:0;width:45px;height:45px;background:linear-gradient(var(--purple-nav),var(--purple-deep))}
.area .icon svg{position:absolute;left:12px;top:13px}
.area h3{position:absolute;left:55px;top:3px;font-weight:400;font-size:12.5px;color:#333;white-space:nowrap}
.area span{position:absolute;left:55px;top:25px;font-size:9px;color:#777;white-space:nowrap}
.quote-band{position:absolute;top:1006px;left:0;width:1024px;height:88px;background:var(--band);border-top:1px solid var(--line)}
.quote-band p{position:absolute;top:30px;left:130px;width:764px;text-align:center;font-style:italic;font-weight:300;font-size:12.5px;line-height:19px;color:#6a7e90}
.quote-band b{font-style:normal;font-weight:500;color:#5a6a7a}
.footer{position:absolute;top:1094px;left:0;width:1024px;height:79px;background:var(--white)}
.footer .brand{left:137px;top:14px}
.footer .brand .name{font-size:30px;line-height:32px}
.footer .brand .tag{font-size:15px;line-height:18px;margin-left:53px}
.contact{position:absolute;font-size:9px;line-height:17.5px;color:#666}
.contact svg{position:absolute;left:0;top:3px}
.contact-addr{left:455px;top:17px;padding-left:18px}
.contact-tel{left:585px;top:17px;padding-left:19px}
.follow{position:absolute;left:776px;top:17px;font-size:9px;color:#666}
.social{position:absolute;top:36px;width:26px;height:26px}
.social-a{left:778px;background:#2a5aa8}
.social-b{left:816px;background:#1aa3dc}
.social-c{left:855px;background:#1779b5}
.bottombar{position:absolute;top:1173px;left:0;width:1024px;height:27px;background:var(--purple)}
.bottombar .copy{position:absolute;left:137px;top:7px;font-size:9.5px;color:var(--white)}
.bottombar a{position:absolute;top:7px;font-size:9.5px;color:var(--white);text-decoration:none}
</style>
</head>
<body>
<div class="topline"></div>
<header class="header">
  <div class="brand"><span class="name">Dunmore + Willett</span><span class="tag">Solicitors</span></div>
  <div class="reg reg-auth"><small>Regulation Authority</small><b>NO.731508</b></div>
  <div class="reg reg-vat"><small>VAT registered number:</small><b>418 2270 56</b></div>
</header>
<nav class="nav">
  <a class="active" href="#">Home</a>
  <a style="left:298px" href="#">Areas of Expertise</a>
  <a style="left:442px" href="#">Daniel Dunmore</a>
  <a style="left:566px" href="#">Peter Willett</a>
  <a style="left:691px" href="#">Contact Us</a>
</nav>
<section class="hero" role="img" aria-label="Night-time city skyline beside a lit suspension bridge under a purple dusk sky">
  <div class="glow"></div>
  <h1>Dunmore and Willett Solicitors,<br>for the service you deserve.</h1>
</section>
<article class="card card-a">
  <div class="photo" role="img" aria-label="Portrait photograph of Daniel Dunmore"></div>
  <h2>Daniel Dunmore</h2>
  <p>Daniel Dunmore qualified as a solicitor in 1987 and spent many years working with a busy commercial practice in North London.</p>
  <span class="more">Read More</span>
</article>
<article class="card card-b">
  <div class="photo" role="img" aria-label="Black and white portrait photograph of Peter Willett"></div>
  <h2>Peter Willett</h2>
  <p>Willett has 40 years experience in the law. He has a wide range of expertise in commercial and private client matters</p>
  <span class="more">Read More</span>
</article>
<h2 class="expertise-title">Our Areas of Expertise</h2>
<p class="expertise-intro">The point of using Lorem Ipsum is that it has a more-or-less normal distribution of letters, as opposed to using 'Content here, content here', making it look like readable English.</p>

<svg width="0" height="0" style="position:absolute"><defs><g id="case"><rect x="1" y="5" width="19" height="14" rx="2" fill="#fff"/><rect x="7" y="1.5" width="7" height="4" rx="1" fill="none" stroke="#fff" stroke-width="1.6"/><rect x="1" y="11" width="19" height="1.4" fill="#5d4899"/><rect x="8.5" y="10" width="4" height="3.4" fill="#fff" stroke="#5d4899" stroke-width=".8"/></g></defs></svg>

<div class="area" style="left:136px;top:808px"><div class="icon"><svg width="21" height="20"><use href="#case"/></svg></div><h3>Litigation</h3><span>Private and commercial</span></div>
<div class="area" style="left:329px;top:808px"><div class="icon"><svg width="21" height="20"><use href="#case"/></svg></div><h3>Company Matters</h3><span>Acquisitions &amp; mergers</span></div>
<div class="area" style="left:519px;top:808px"><div class="icon"><svg width="21" height="20"><use href="#case"/></svg></div><h3>Insolvency</h3><span>Private and commercial</span></div>
<div class="area" style="left:712px;top:808px"><div class="icon"><svg width="21" height="20"><use href="#case"/></svg></div><h3>Conveyancing</h3><span>Commercial and Residential</span></div>
<div class="area" style="left:136px;top:866px"><div class="icon"><svg width="21" height="20"><use href="#case"/></svg></div><h3>Wills &amp; Probate</h3><span>Estate planning, disputes</span></div>
<div class="area" style="left:329px;top:866px"><div class="icon"><svg width="21" height="20"><use href="#case"/></svg></div><h3>Landlord &amp; Tenant</h3><span>Agreements and disputes</span></div>
<div class="area" style="left:519px;top:866px"><div class="icon"><svg width="21" height="20"><use href="#case"/></svg></div><h3>Divorce</h3><span>Ancillary relief, children</span></div>
<div class="area" style="left:712px;top:866px"><div class="icon"><svg width="21" height="20"><use href="#case"/></svg></div><h3>Care of the Elderly</h3><span>Powers of Attorney</span></div>
<div class="area" style="left:136px;top:924px"><div class="icon"><svg width="21" height="20"><use href="#case"/></svg></div><h3>Intellectual Property</h3><span>Copyright, patents</span></div>
<div class="area" style="left:329px;top:924px"><div class="icon"><svg width="21" height="20"><use href="#case"/></svg></div><h3>Commercial Crime</h3><span>'White Collar' crime</span></div>
<div class="area" style="left:519px;top:924px"><div class="icon"><svg width="21" height="20"><use href="#case"/></svg></div><h3>Media Law</h3><span>Film, TV, Theatre, Radio</span></div>
<div class="area" style="left:712px;top:924px"><div class="icon"><svg width="21" height="20"><use href="#case"/></svg></div><h3>Commercial / Business</h3><span>Structures, agreements</span></div>

<section class="quote-band">
  <p>“The point of using Lorem Ipsum is that it has a more-or-less normal distribution of letters, as opposed to using 'Content here, content here', making it look like readable English.” -<b>Jane Marsh, Halden Group</b></p>
</section>
<footer class="footer">
  <div class="brand"><span class="name">Dunmore + Willett</span><span class="tag">Solicitors</span></div>
  <div class="contact contact-addr">
    <svg width="10" height="13" viewBox="0 0 10 13"><path d="M5 0a5 5 0 0 1 5 5c0 3.5-5 8-5 8S0 8.5 0 5a5 5 0 0 1 5-5z" fill="#4f3a86"/><circle cx="5" cy="5" r="1.8" fill="#fff"/></svg>
    Company Name<br>48 Harbour Lane<br>Riverton, NY 10999
  </div>
  <div class="contact contact-tel">
    <svg width="11" height="11" viewBox="0 0 11 11"><path d="M2 0l2 2.5-1.2 1.4a7 7 0 0 0 4.3 4.3L8.5 7 11 9l-1.5 2C4.5 11 0 6.5 0 1.5z" fill="#4f3a86"/></svg>
    Phone: +123 555 0142<br>
    <svg width="11" height="9" viewBox="0 0 11 9" style="top:21px"><rect width="11" height="9" fill="#4f3a86"/><path d="M0 0l5.5 4.5L11 0" fill="none" stroke="#fff"/></svg>
    contact@dunmorewillett.example
  </div>
  <div class="follow">Follow Us</div>
  <div class="social social-a" aria-label="Social link"></div>
  <div class="social social-b" aria-label="Social link"></div>
  <div class="social social-c" aria-label="Social link"></div>
</footer>
<div class="bottombar">
  <span class="copy">Copyright 2014 Dunmore + Willett | All Rights Reserved</span>
  <a style="left:604px" href="#">Home</a>
  <a style="left:655px" href="#">Services</a>
  <a style="left:703px" href="#">Locations</a>
  <a style="left:764px" href="#">Partners</a>
  <a style="left:820px" href="#">FAQ</a>
  <a style="left:856px" href="#">Contact</a>
</div>
</body>
</html>
```